Hi,

I would like to have a invitation made for a party. exactly like the picture in the link below.

http://pinboardia.example/pin/730215948361027459/

However, Please change the colors into fun/ girly feeling. font can be different and size of the card should be the same

Name of the girl: RINA
What: Bachelorette Party
Where:TOLO Boat
Dubai Coral Quay Sailing Club
When:7th of February 2013

No RSVP required. (so no need to put it)

```html
<!DOCTYPE html>
<html lang="en">
<head>
<meta charset="utf-8">
<title>Rina's Bachelorette Party Invitation</title>
<link rel="stylesheet" href="https://fonts.googleapis.com/css2?family=Cinzel+Decorative:wght@900&family=Fira+Sans:wght@600&family=Rye&family=Uncial+Antiqua&family=Almendra&display=swap">
<style>
  :root {
    --sky: #7fd0f7;
    --mauve: #966b7e;
    --ink: #111111;
    --paper: #ffffff;
    --edge: #333333;
  }
  * { margin: 0; padding: 0; box-sizing: border-box; }
  html, body {
    width: 1200px; height: 900px; overflow: hidden;
    background: var(--paper);
  }
  .canvas { position: relative; width: 1200px; height: 900px; }

  .invitation {
    position: absolute; left: 17px; top: 151px;
    width: 1164px; height: 550px;
    display: flex;
  }
  .panel {
    position: relative; height: 100%;
    border: 1px solid var(--edge);
  }
  .panel + .panel { border-left: none; }
  .panel--title { width: 387px; background: var(--sky); }
  .panel--feature { width: 388px; background: var(--mauve); }
  .panel--details { width: 389px; background: var(--sky); }

  .ornament {
    position: absolute;
    background: var(--ink);
    opacity: 0.85;
    border-radius: 40% 60% 45% 55%;
  }
  .ornament--top-corner { left: 280px; top: 4px; width: 100px; height: 80px; }
  .ornament--bottom-corner { left: 8px; top: 458px; width: 92px; height: 82px; }
  .ornament--swirl-left { left: 14px; top: 104px; width: 165px; height: 82px; }
  .ornament--swirl-right { left: 205px; top: 104px; width: 170px; height: 82px; }

  .guest-name {
    position: absolute; left: 0; width: 387px; top: 92px;
    text-align: center;
    font-family: "Cinzel Decorative", serif; font-weight: 900;
    font-size: 76px; line-height: 1; color: var(--ink);
    white-space: nowrap;
  }
  .tagline {
    position: absolute; top: 198px; width: 100%;
    text-align: center; white-space: nowrap;
    font-family: "Fira Sans", sans-serif; font-weight: 600;
    font-size: 37px; line-height: 1; letter-spacing: 0.5px;
  }
  .panel--title .tagline { color: var(--mauve); }
  .panel--feature .tagline { color: var(--sky); }

  .headline {
    position: absolute; top: 232px; width: 100%;
    text-align: center; white-space: nowrap;
    font-family: "Rye", serif;
    font-size: 150px; line-height: 1;
    letter-spacing: -4px;
    transform: scaleY(1.42); transform-origin: top center;
    -webkit-text-stroke: 3px var(--ink);
    text-shadow: 1px 1px 0 var(--ink), 2px 2px 0 var(--ink), 3px 3px 0 var(--ink),
                 4px 4px 0 var(--ink), 5px 5px 0 var(--ink), 6px 6px 0 var(--ink),
                 7px 6px 0 var(--ink), 8px 7px 0 var(--ink), 9px 7px 0 var(--ink);
  }
  .panel--title .headline { color: var(--sky); }
  .panel--feature .headline { color: var(--mauve); }

  .details { position: absolute; inset: 0; text-align: center; color: var(--ink); }
  .details__label, .details__value {
    position: absolute; left: 0; width: 100%; white-space: nowrap; line-height: 1;
  }
  .details__label { font-family: "Uncial Antiqua", serif; font-size: 32px; }
  .details__value { font-family: "Almendra", serif; font-size: 38px; }
  .details__value--small { font-size: 32px; }
</style>
</head>
<body>
<div class="canvas">
  <section class="invitation">
    <div class="panel panel--title">
      <div class="ornament ornament--top-corner" role="img" aria-label="Black floral corner flourish"></div>
      <h1 class="guest-name">RINA’S</h1>
      <p class="tagline">LAST CHANCE TO</p>
      <p class="headline">SIN</p>
      <div class="ornament ornament--bottom-corner" role="img" aria-label="Black floral corner flourish"></div>
    </div>

    <div class="panel panel--feature">
      <div class="ornament ornament--swirl-left" role="img" aria-label="Black floral vine swirl"></div>
      <div class="ornament ornament--swirl-right" role="img" aria-label="Black floral vine swirl"></div>
      <p class="tagline">CELEBRATE BEING</p>
      <p class="headline">GLE</p>
    </div>

    <div class="panel panel--details">
      <div class="details">
        <p class="details__label" style="top:12px">WHO</p>
        <p class="details__value" style="top:70px">Rina Alsayed</p>
        <p class="details__label" style="top:141px">WHAT</p>
        <p class="details__value details__value--small" style="top:206px">Bachelorette Party!</p>
        <p class="details__label" style="top:274px">WHERE</p>
        <p class="details__value details__value--small" style="top:333px">TOLO Boat Dubai</p>
        <p class="details__value details__value--small" style="top:378px">Coral Quay Sailing Club</p>
        <p class="details__label" style="top:441px">WHEN</p>
        <p class="details__value details__value--small" style="top:496px">7th of February 2013</p>
      </div>
    </div>
  </section>
</div>
</body>
</html>
```